Brantoe Art

A website showing drawings, thumbnails and full size with space for asize and adescription . With the ability to expand for more pictures and purchase through PayPal online. I already own www.brantoeart.com

```html
<!DOCTYPE html>
<html lang="en">
<head>
<meta charset="utf-8">
<title>Brantoe Art – Gallery</title>
<link rel="stylesheet" href="https://fonts.googleapis.com/css2?family=Roboto:wght@300;400;500&family=Arvo:wght@700&display=swap">
<style>
:root{
  --teal:#2b6b61;
  --teal-dark:#1f5a52;
  --sky:#a7d7e5;
  --paper:#fdfaf8;
  --ink:#111;
  --frame:#08131a;
  --alert:#f01010;
  --leaf-1:#0f4a5a;
  --leaf-2:#3c8ea0;
  --leaf-3:#b9dbe0;
  --leaf-4:#cfe3cf;
}
*{box-sizing:border-box;margin:0;padding:0}
html,body{width:1200px;height:1200px;overflow:hidden}
body{position:relative;font-family:"Roboto",sans-serif;background:var(--leaf-1)}
.backdrop{position:absolute;inset:0;
  background:
    radial-gradient(ellipse at 20% 75%,var(--leaf-4) 0%,transparent 45%),
    radial-gradient(ellipse at 55% 10%,var(--leaf-3) 0%,transparent 40%),
    linear-gradient(160deg,var(--leaf-1) 0%,var(--leaf-2) 45%,var(--leaf-1) 70%,var(--leaf-2) 100%);}
.topbar{position:absolute;left:80px;top:0;width:1041px;height:51px;background:var(--paper);
  color:var(--teal);font-size:14px;letter-spacing:1px}
.topbar .welcome{position:absolute;left:23px;top:17px}
.topbar .contact{position:absolute;left:652px;top:16px;display:flex;align-items:center;gap:8px}
.topbar .contact svg{width:20px;height:20px}
.topbar .contact .gap{width:14px}
.cart-badge{position:absolute;left:1109px;top:10px;width:35px;height:35px;border-radius:50%;
  background:var(--alert);color:#fff;font-size:14px;display:flex;align-items:center;justify-content:center}
.navband{position:absolute;left:80px;top:51px;width:1041px;height:74px;background:var(--sky)}
.navband a{position:absolute;top:29px;color:var(--teal);text-decoration:none;font-size:14.5px;letter-spacing:1.2px;font-weight:500}
.brand{position:absolute;left:480px;top:15px;width:224px;height:152px;border-radius:50%;
  background:var(--paper);box-shadow:0 4px 10px rgba(0,0,0,.35);display:flex;align-items:center;justify-content:center}
.brand span{font-size:30px;font-weight:500;color:var(--teal);text-align:center;line-height:1}
.quote{position:absolute;left:0;width:1200px;top:232px;text-align:center;color:#fff;
  font-family:"Arvo",serif;font-weight:700;text-shadow:2px 2px 4px rgba(0,0,0,.6)}
.quote p{font-size:51px;line-height:68px;letter-spacing:-1px}
.quote cite{display:block;font-style:normal;font-size:25px;margin-top:20px}
.panel{position:absolute;left:80px;top:480px;width:1041px;height:620px;background:var(--paper)}
.panel h1{position:absolute;top:22px;width:100%;text-align:center;font-weight:400;font-size:60px;color:var(--teal);line-height:1}
.panel h2{position:absolute;top:79px;width:100%;text-align:center;font-weight:400;font-size:28px;color:var(--ink)}
.card{position:absolute;top:150px;width:260px}
.card .frame{width:260px;height:289px;background:var(--frame);padding:12px}
.card .art{width:228px;height:228px}
.card h3{font-weight:400;font-size:27px;margin:9px 0 0 4px;color:var(--ink)}
.card p{font-size:13.5px;text-align:center;width:240px;margin-top:10px;line-height:16px;color:var(--ink)}
.card .actions{display:flex;justify-content:space-between;align-items:center;margin-top:12px;padding:0 8px 0 3px;font-size:11.5px}
.card .actions span{display:flex;align-items:center;gap:6px}
.view-more{position:absolute;top:582px;width:100%;text-align:center;font-size:16px;color:var(--teal)}
.footer{position:absolute;left:80px;top:1115px;width:1041px;height:74px;background:var(--sky);
  display:flex;align-items:center;justify-content:center;color:var(--teal-dark);font-size:13.5px}
</style>
</head>
<body>
<div class="backdrop" role="img" aria-label="Photograph of large teal and blue tropical leaves"></div>

<header class="topbar">
  <span class="welcome">Welcome to Brantoeart.com</span>
  <div class="contact">
    <svg viewBox="0 0 20 20" fill="none" stroke="currentColor" stroke-width="1.6"><path d="M5 2l3 4-2 2c1 2 3 4 5 5l2-2 4 3-2 3C9 17 3 11 2 4z"/></svg>
    <span>123-555-0147</span><span class="gap"></span>
    <svg viewBox="0 0 20 20" fill="currentColor"><path d="M2 6l8-4 8 4v11H2z"/><path d="M2 7l8 6 8-6" stroke="#fff" stroke-width="1.3" fill="none"/></svg>
    <span>info@brantoeart.com</span><span class="gap"></span>
    <svg viewBox="0 0 20 20" fill="none" stroke="#222" stroke-width="1.5"><path d="M2 3h3l2 10h9l2-7H6"/><circle cx="8" cy="16" r="1.3"/><circle cx="15" cy="16" r="1.3"/></svg>
  </div>
</header>
<div class="cart-badge">0</div>

<nav class="navband">
  <a href="#" style="left:51px">Home</a>
  <a href="#" style="left:147px">About Brantoe</a>
  <a href="#" style="left:275px">Gallery</a>
  <a href="#" style="left:672px">Testimonials</a>
  <a href="#" style="left:799px">Events</a>
  <a href="#" style="left:895px">Contact Us</a>
</nav>
<div class="brand"><span>Brantoe<br>Art</span></div>

<section class="quote">
  <p>ART IS NOT WHAT YOU SEE.</p>
  <p>BUT WHAT YOU MAKE OTHERS SEE.</p>
  <cite>- EDMOND VAREL</cite>
</section>

<main class="panel">
  <h1>brantoe art</h1>
  <h2>Gallery</h2>

  <article class="card" style="left:42px">
    <div class="frame"><div class="art" role="img" aria-label="Abstract cubist painting in red, blue and yellow" style="background:linear-gradient(135deg,#d2561e,#1c2a8a 50%,#e2b01c)"></div></div>
    <h3>Artist name</h3>
    <p>work temper will come here with short description</p>
    <div class="actions"><span>View details</span><span><svg width="18" height="18" viewBox="0 0 20 20" fill="none" stroke="#222" stroke-width="1.4"><path d="M2 3h3l2 10h9l2-7H6"/><circle cx="8" cy="16" r="1.3"/><circle cx="15" cy="16" r="1.3"/></svg>Add to Cart</span></div>
  </article>

  <article class="card" style="left:399px">
    <div class="frame"><div class="art" role="img" aria-label="Painting of a red rose with teal leaves" style="background:radial-gradient(circle at 60% 50%,#e0383a 0%,#c86a5a 35%,#4a8a8c 75%,#2d3a44 100%)"></div></div>
    <h3>Artist name</h3>
    <p>work temper will come here with short description</p>
    <div class="actions"><span>View details</span><span><svg width="18" height="18" viewBox="0 0 20 20" fill="none" stroke="#222" stroke-width="1.4"><path d="M2 3h3l2 10h9l2-7H6"/><circle cx="8" cy="16" r="1.3"/><circle cx="15" cy="16" r="1.3"/></svg>Add to Cart</span></div>
  </article>

  <article class="card" style="left:734px">
    <div class="frame"><div class="art" role="img" aria-label="Colourful abstract portrait painting" style="background:linear-gradient(120deg,#1a8a5a,#d8304a 40%,#2a5ad0 70%,#e0a020)"></div></div>
    <h3>Artist name</h3>
    <p>work temper will come here with short description</p>
    <div class="actions"><span>View details</span><span><svg width="18" height="18" viewBox="0 0 20 20" fill="none" stroke="#222" stroke-width="1.4"><path d="M2 3h3l2 10h9l2-7H6"/><circle cx="8" cy="16" r="1.3"/><circle cx="15" cy="16" r="1.3"/></svg>Add to Cart</span></div>
  </article>

  <div class="view-more">View more...</div>
</main>

<footer class="footer">Copyright 2019, brantoeart.co. All Rights Reserved.</footer>
</body>
</html>
```